Business Card Design

Need business card design for all carpentry & construction solutions. We would like to see designs that use black as a background with orange writing as it would stand out.

Business

KRV CONTRACTING
MARTIN COLBY
14 PELLINGTON ST
CORVAN HILLS
NX 4417
0498371265
krvcontracting@tramlex.com

```html
<!DOCTYPE html>
<html lang="en">
<head>
<meta charset="utf-8">
<title>KRV Contracting – Business Card</title>
<link rel="stylesheet" href="https://fonts.googleapis.com/css2?family=Bebas+Neue&family=Arimo&display=swap">
<style>
  :root {
    --sheet: #ffffff;
    --green: #55b84d;
    --orange: #f27a2c;
    --ink: #3f3f3f;
    --ghost-on-green: #b2a8a4;
    --ghost-on-orange: #8d8581;
    --label: #111111;
    --white: #ffffff;
  }
  html, body {
    margin: 0;
    padding: 0;
    width: 1200px;
    height: 1200px;
    overflow: hidden;
    background: var(--sheet);
  }
  .sheet {
    position: relative;
    width: 1200px;
    height: 1200px;
  }
  .side-label {
    position: absolute;
    left: 0;
    width: 1160px;
    text-align: center;
    font-family: "Arimo", sans-serif;
    font-weight: 400;
    font-size: 50px;
    letter-spacing: 5px;
    color: var(--label);
    margin: 0;
    line-height: 1;
  }
  .side-label--front { top: 4px; }
  .side-label--back { top: 592px; }

  .card {
    position: absolute;
    left: 122px;
    width: 920px;
    height: 518px;
    overflow: hidden;
    box-shadow: 8px 8px 14px rgba(0,0,0,0.28);
  }
  .card--front { top: 66px; }
  .card--back { top: 655px; }

  /* front */
  .band { position: absolute; left: 0; width: 100%; overflow: hidden; }
  .band--green { top: 0; height: 279px; background: var(--green); }
  .band--orange { top: 279px; height: 239px; background: var(--orange); }

  .ghost {
    position: absolute;
    font-family: "Bebas Neue", sans-serif;
    line-height: 1;
    white-space: nowrap;
    margin: 0;
  }
  .ghost--initials {
    left: 40px;
    bottom: -66px;
    font-size: 420px;
    letter-spacing: 22px;
    color: var(--ghost-on-green);
  }
  .ghost--letter {
    top: -34px;
    font-size: 450px;
    color: var(--ghost-on-orange);
  }
  .ghost--c { left: -40px; }
  .ghost--o { left: 150px; }
  .ghost--n { left: 478px; }
  .ghost--t { left: 747px; }

  .company, .person {
    position: absolute;
    left: 26px;
    margin: 0;
    font-family: "Bebas Neue", sans-serif;
    font-weight: 400;
    color: var(--ink);
    line-height: 1;
    white-space: nowrap;
  }
  .company { top: 18px; font-size: 98px; letter-spacing: 0.2em; }
  .person { top: 135px; font-size: 78px; letter-spacing: 0.25em; }

  .contact {
    position: absolute;
    left: 112px;
    top: 310px;
    margin: 0;
    font-family: "Bebas Neue", sans-serif;
    font-style: normal;
    font-size: 43px;
    line-height: 39px;
    letter-spacing: 0.24em;
    color: var(--ink);
    white-space: nowrap;
  }
  .contact span { display: block; }

  .icon { position: absolute; left: 30px; }
  .icon--pin { top: 313px; }
  .icon--phone { top: 410px; }
  .icon--mail { top: 463px; }
</style>
</head>
<body>
<main class="sheet">
  <h2 class="side-label side-label--front">Front</h2>

  <section class="card card--front" aria-label="Business card front">
    <div class="band band--green">
      <p class="ghost ghost--initials" aria-hidden="true">KRV</p>
    </div>
    <div class="band band--orange" aria-hidden="true">
      <p class="ghost ghost--letter ghost--c">C</p>
      <p class="ghost ghost--letter ghost--o">O</p>
      <p class="ghost ghost--letter ghost--n">N</p>
      <p class="ghost ghost--letter ghost--t">T</p>
    </div>

    <h1 class="company">KRV CONTRACTING</h1>
    <p class="person">MARTIN COLBY</p>

    <svg class="icon icon--pin" width="40" height="52" viewBox="0 0 40 52" aria-hidden="true">
      <path d="M20 2C10 2 3 9.5 3 19c0 12 17 31 17 31s17-19 17-31C37 9.5 30 2 20 2z" fill="var(--white)"/>
      <circle cx="20" cy="18" r="6" fill="none" stroke="var(--ink)" stroke-width="3"/>
    </svg>

    <svg class="icon icon--phone" width="48" height="44" viewBox="0 0 48 44" aria-hidden="true">
      <path d="M10 3c3-1 5 0 6 2l4 8c1 2 0 4-2 5l-3 2c2 6 7 11 13 14l2-3c1-2 3-3 5-2l8 4c2 1 3 3 2 6l-2 3c-2 2-5 3-8 2C21 40 8 28 4 14 3 11 4 8 6 6z" fill="var(--white)"/>
    </svg>

    <svg class="icon icon--mail" width="50" height="40" viewBox="0 0 50 40" aria-hidden="true">
      <path d="M2 16 L25 2 L48 16 V38 H2 Z" fill="var(--white)"/>
      <path d="M2 16 L25 30 L48 16" fill="none" stroke="var(--orange)" stroke-width="2"/>
      <circle cx="25" cy="16" r="6" fill="none" stroke="var(--orange)" stroke-width="2"/>
    </svg>

    <address class="contact">
      <span>14 PELLINGTON ST</span>
      <span>CORVAN HILLS</span>
      <span>NX 4417</span>
      <span>0498371265</span>
      <span>KRVCONTRACTING@TRAMLEX.COM</span>
    </address>
  </section>

  <h2 class="side-label side-label--back">back</h2>

  <section class="card card--back" aria-label="Business card back">
    <svg width="920" height="518" viewBox="0 0 920 518">
      <defs>
        <linearGradient id="frame-tone" x1="0" y1="0" x2="1" y2="1">
          <stop offset="0" stop-color="#2f4a2c"/>
          <stop offset="0.35" stop-color="#5f9a57"/>
          <stop offset="0.7" stop-color="#7fb274"/>
          <stop offset="1" stop-color="#24361f"/>
        </linearGradient>
        <radialGradient id="machine-tone" cx="0.6" cy="0.55" r="0.7">
          <stop offset="0" stop-color="#c9875a"/>
          <stop offset="0.45" stop-color="#8c5a3c"/>
          <stop offset="1" stop-color="#2e241e"/>
        </radialGradient>
      </defs>
      <polygon points="0,0 595,0 324,518 0,518" fill="url(#frame-tone)"
               role="img" aria-label="Photo of green-toned timber wall and roof framing"/>
      <polygon points="595,0 920,0 920,518 324,518" fill="url(#machine-tone)"
               role="img" aria-label="Photo of an orange digger bucket and earthmoving machine on soil"/>
    </svg>
  </section>
</main>
</body>
</html>
```